Financial Consulting Company in need of technical diagram

Attached is a basic template to follow, however the following changes must be made:
- Get rid of reflection boxes at the bottom
-Delete anything in parentheses
-Change top box to read "Uncover Value Opportunities"
-Change bottom right box to read "Sales and Operations Planning"
-Change bottom left box to read "Financial Planning"

Additionally we would like to see something a little more creative and cohesive. One possibility is using "Cheveron" type arrows to show the "wheel" effect.

Please email mtorvek@halbrine.example if you have any questions!
Updates

Please see newly uploaded image for an example of how we would like it re-created.

Project Deadline Extended

Industry/Entity Type

Financial

Requirements
Must have
• I'm looking for something that keeps the "wheel" approach, but is not a direct re-creation of the example given. The boxes for example, dont' necessarily need to stay boxes. Feel free to play around with placement as well.
Nice to have
• Please see green wheel for example of how it can be re-created.

```html
<!DOCTYPE html>
<html lang="en">
<head>
<meta charset="utf-8">
<title>Value Cycle Wheel</title>
<link rel="stylesheet" href="https://fonts.googleapis.com/css2?family=Questrial&display=swap">
<style>
  :root {
    --page: #ffffff;
    --navy-deep: #0c2463;
    --navy-mid: #1d4f8a;
    --teal-mid: #2f8fa6;
    --mint: #6ff4d2;
    --mint-soft: #5fe0c6;
    --dot: #ffffff;
    --label: #ffffff;
  }
  html, body {
    margin: 0;
    padding: 0;
    width: 1200px;
    height: 900px;
    overflow: hidden;
    background: var(--page);
  }
  .wheel-canvas {
    display: block;
    width: 1200px;
    height: 900px;
  }
  .stage-label {
    font-family: "Questrial", "Helvetica Neue", Arial, sans-serif;
    font-size: 23px;
    fill: var(--label);
    text-anchor: middle;
    letter-spacing: 0.2px;
  }
  .chevron-dot { fill: var(--dot); }
  .stage-rim { fill: none; stroke: var(--page); stroke-width: 9; }
</style>
</head>
<body>
<svg class="wheel-canvas" viewBox="0 0 1200 900" xmlns="http://www.w3.org/2000/svg" role="img" aria-label="Five-stage value cycle wheel">
  <defs>
    <linearGradient id="ringShade" x1="0" y1="0" x2="1" y2="1">
      <stop offset="0" stop-color="var(--navy-deep)"/>
      <stop offset="0.5" stop-color="var(--navy-mid)"/>
      <stop offset="1" stop-color="var(--navy-deep)"/>
    </linearGradient>
    <linearGradient id="stageShade" x1="0.85" y1="0.1" x2="0.15" y2="0.95">
      <stop offset="0" stop-color="var(--mint)"/>
      <stop offset="0.5" stop-color="var(--mint-soft)"/>
      <stop offset="1" stop-color="var(--teal-mid)"/>
    </linearGradient>
    <g id="chevron">
      <circle class="chevron-dot" cx="-13" cy="-26" r="6.5"/>
      <circle class="chevron-dot" cx="0" cy="-13" r="6.5"/>
      <circle class="chevron-dot" cx="13" cy="0" r="6.5"/>
      <circle class="chevron-dot" cx="0" cy="13" r="6.5"/>
      <circle class="chevron-dot" cx="-13" cy="26" r="6.5"/>
    </g>
  </defs>

  <!-- connecting band -->
  <circle class="wheel-band" cx="615" cy="470" r="298" fill="none" stroke="url(#ringShade)" stroke-width="125"/>

  <!-- direction chevrons -->
  <g class="direction-markers">
    <use href="#chevron" transform="translate(512 152) rotate(-18)"/>
    <use href="#chevron" transform="translate(842 268) rotate(48)"/>
    <use href="#chevron" transform="translate(842 628) rotate(124)"/>
    <use href="#chevron" transform="translate(494 736) rotate(204)"/>
    <use href="#chevron" transform="translate(296 436) rotate(276)"/>
  </g>

  <!-- stages -->
  <g class="stage stage-uncover">
    <circle cx="688" cy="160" r="98" fill="url(#stageShade)"/>
    <circle class="stage-rim" cx="688" cy="160" r="102"/>
    <text class="stage-label" x="680" y="125">Uncover</text>
    <text class="stage-label" x="680" y="155">Value</text>
    <text class="stage-label" x="680" y="185">Opportunities</text>
  </g>
  <g class="stage stage-strategize">
    <circle cx="910" cy="432" r="105" fill="url(#stageShade)"/>
    <circle class="stage-rim" cx="910" cy="432" r="109"/>
    <text class="stage-label" x="895" y="411">Strategize</text>
    <text class="stage-label" x="895" y="441">and</text>
    <text class="stage-label" x="895" y="471">Align</text>
  </g>
  <g class="stage stage-sales">
    <circle cx="718" cy="730" r="107" fill="url(#stageShade)"/>
    <circle class="stage-rim" cx="718" cy="730" r="111"/>
    <text class="stage-label" x="720" y="718">Sales and</text>
    <text class="stage-label" x="720" y="748">Operations</text>
    <text class="stage-label" x="720" y="778">Planning</text>
  </g>
  <g class="stage stage-financial">
    <circle cx="362" cy="645" r="105" fill="url(#stageShade)"/>
    <circle class="stage-rim" cx="362" cy="645" r="109"/>
    <text class="stage-label" x="366" y="640">Financial</text>
    <text class="stage-label" x="366" y="670">Planning</text>
  </g>
  <g class="stage stage-assess">
    <circle cx="342" cy="285" r="108" fill="url(#stageShade)"/>
    <circle class="stage-rim" cx="342" cy="285" r="112"/>
    <text class="stage-label" x="344" y="277">Assess the</text>
    <text class="stage-label" x="344" y="307">Results</text>
  </g>
</svg>
</body>
</html>
```